Band and Coaching business card (creative industry)

My company The Birch Ensemble is the name of my band Soul outfit but is also a brand I use for my coaching business which is Performance coaching in the following areas: Corporate coaching, acting, vocals and dialect. The band plays for corporate events and private functions as well as local bar/restaurant/festivals.

Hi All

Please see updated info for the wording of the business card front and back.  This is ito then be followed with contact number, email and facebook link

first side should have:

Rosalind Pettigrew
Creative Director
( followed by contact info as per previous)

Side 2:

The Birch Ensemble  - Band  
 Vocalist      I   Musician    I  Songwriter

The Birch Ensemble  - Studio
Performance Coaching  
Acting  I  Vocals  I Dialect  I Corporate Coaching

Industry/Entity Type

Events

Contact Information for Business Card

The Birch Ensemble (logo)
Rosalind Pettigrew
Musician/Vocalist/Performance Coach
M: 0412 655 918
E: thebirchensemble@mailpost.example
W: www.socialpage.example/thebirchensembleband

Font styles to use
Sans Serif

Requirements
Must have
• first side should have:

Rosalind Pettigrew
Creative Director

Side 2:

The Birch Ensemble - Band
Vocalist I Musician I Songwriter

The Birch Ensemble - Studio
Performance Coaching
Acting I Vocals I Dialect I Corporate Coaching
Nice to have
• I like smaller business cards with curved edges.

some ideas for look in additional business cards attached.
Should not have
• music notes or anything specific to the field. Want to keep it funky and contemporary

```html
<!DOCTYPE html>
<html lang="en">
<head>
<meta charset="utf-8">
<title>Rosalind Pettigrew – Business Card</title>
<link rel="stylesheet" href="https://fonts.googleapis.com/css2?family=Yanone+Kaffeesatz:wght@500&family=Source+Sans+3:wght@400;600&display=swap">
<style>
  :root {
    --magenta: #e0388c;
    --plum: #ae3a8e;
    --violet: #8d4a96;
    --contact: #b13a8c;
    --paper: #ffffff;
    --backdrop: #ffffff;
  }
  html, body {
    margin: 0;
    padding: 0;
    width: 1200px;
    height: 607px;
    overflow: hidden;
    background: var(--backdrop);
  }
  .card {
    position: absolute;
    left: 18px;
    top: 11px;
    width: 1162px;
    height: 584px;
    box-sizing: border-box;
    border: 2px solid var(--plum);
    border-radius: 30px;
    background: var(--paper);
    overflow: hidden;
    font-family: "Source Sans 3", sans-serif;
  }
  .card__band {
    position: absolute;
    inset: 0;
    width: 100%;
    height: 100%;
  }
  .card__band polygon { fill: var(--plum); }
  .identity {
    position: absolute;
    left: 80px;
    top: 130px;
    display: inline-flex;
    flex-direction: column;
    align-items: flex-end;
  }
  .identity__name {
    margin: 0;
    font-family: "Yanone Kaffeesatz", sans-serif;
    font-weight: 500;
    font-size: 72px;
    line-height: 1;
    color: var(--magenta);
    letter-spacing: 0.5px;
  }
  .identity__role {
    margin: 2px 0 0;
    font-size: 22px;
    color: var(--violet);
  }
  .contacts {
    position: absolute;
    left: 85px;
    top: 296px;
    height: 177px;
    margin: 0;
    padding: 0 0 0 28px;
    list-style: none;
    border-left: 3px solid var(--magenta);
    display: flex;
    flex-direction: column;
    justify-content: space-between;
  }
  .contacts__item {
    display: flex;
    align-items: center;
    gap: 8px;
    font-size: 24px;
    line-height: 30px;
    color: var(--contact);
  }
  .contacts__icon {
    width: 26px;
    height: 26px;
    flex: none;
    fill: var(--contact);
  }
  .brand {
    position: absolute;
    left: 705px;
    top: 246px;
    width: 288px;
    height: 288px;
    border-radius: 50%;
    background: var(--magenta);
    display: flex;
    align-items: center;
    justify-content: center;
    text-align: center;
  }
  .brand__name {
    font-family: "Source Sans 3", sans-serif;
    font-weight: 600;
    font-size: 38px;
    line-height: 1.1;
    color: var(--paper);
  }
</style>
</head>
<body>
  <div class="card">
    <svg class="card__band" viewBox="0 0 1162 584" preserveAspectRatio="none" aria-hidden="true">
      <polygon points="667,0 1162,0 1162,584 753,584 956,130"/>
    </svg>

    <div class="identity">
      <h1 class="identity__name">Rosalind Pettigrew</h1>
      <p class="identity__role">Creative Director</p>
    </div>

    <ul class="contacts">
      <li class="contacts__item">
        <svg class="contacts__icon" viewBox="0 0 24 24" aria-hidden="true"><path d="M6.6 2.5c.6-.4 1.4-.3 1.8.3l2.1 3.2c.4.6.3 1.3-.2 1.8L9 9c.7 2.3 2.6 4.6 4.9 5.9l1.3-1.2c.5-.5 1.3-.5 1.8-.1l3 2.3c.6.4.7 1.3.2 1.8l-1.6 1.9c-.8.9-2.1 1.3-3.3.9C9.5 18.8 5 13.9 3.9 7.6c-.2-1.2.3-2.4 1.3-3.1z"/></svg>
        <span>:0412 655 918</span>
      </li>
      <li class="contacts__item">
        <svg class="contacts__icon" viewBox="0 0 24 24" aria-hidden="true"><path d="M2 5h20v14H2zM3.5 6.5 12 13l8.5-6.5"/><path d="M3.5 6.5 12 13l8.5-6.5" fill="none" stroke="#fff" stroke-width="1.6"/></svg>
        <span>:rosalind@thebirchensemble.example</span>
      </li>
      <li class="contacts__item">
        <svg class="contacts__icon" viewBox="0 0 24 24" aria-hidden="true"><circle cx="12" cy="12" r="10"/><g fill="none" stroke="#fff" stroke-width="1.4"><ellipse cx="12" cy="12" rx="4.5" ry="10"/><path d="M2 12h20M4 7h16M4 17h16M12 2v20"/></g></svg>
        <span>:www.thebirchensemble.example</span>
      </li>
      <li class="contacts__item">
        <svg class="contacts__icon" viewBox="0 0 24 24" aria-hidden="true"><rect x="7" y="7" width="10" height="10"/></svg>
        <span>:www.socialpage.example/thebirchensembleband</span>
      </li>
    </ul>

    <div class="brand">
      <span class="brand__name">The Birch<br>Ensemble</span>
    </div>
  </div>
</body>
</html>
```